Tradeline Summit & Expo xmas banner/MREC promotion

Size:
• Leader board: 728 x 90 px
• MREC: 300 x250 px
• Half-page: 300 x 600
• Wide skyscraper: 160 x 600
Image:
Candy cane stripes as the background – image bought. Horizontal or vertical whatever you think will works.
White strip/background for the copy? See images example – unless you don’t need to do that?
Bold font which is "neutra" to our other banners attached. I think black font would look good.
Message:
Please give it a good readable pace between slides – 3 secs?
1st Slide
It’s silly season!
2nd Slide
Treat yourself to an end of year gift
3rd Slide
Book your ticket now and save $$$
4th Slide
Get spoilt. You’re worth it!
5th Slide
Tradeline logo
Target Market(s)
anyone that sells online
• Automotive • Advertising • Digital • Entertainment
• Finance • Hospitality • Pharmaceutical/Healthcare • Pop Culture
• Retail • Travel • Telecommunications

```html
<!DOCTYPE html>
<html lang="en">
<head>
<meta charset="utf-8">
<title>Tradeline Summit &amp; Expo – Holiday Banner Set</title>
<link rel="stylesheet" href="https://fonts.googleapis.com/css2?family=Josefin+Sans:wght@400;700&display=swap">
<style>
  :root {
    --page-bg: #f1ece6;
    --copy-teal: #1b9ab6;
    --strip-white: #ffffff;
    --strip-offwhite: #f8f6f2;
    --stripe-red: #c9252c;
    --stripe-cream: #efe2dc;
    --brand-ink: #2e2e2e;
  }
  * { box-sizing: border-box; margin: 0; padding: 0; }
  html, body {
    width: 1200px; height: 900px; overflow: hidden;
    background: var(--page-bg);
  }
  .stage {
    position: relative;
    width: 1024px; height: 768px;
    transform: scale(1.171875);
    transform-origin: 0 0;
    font-family: "Josefin Sans", sans-serif;
  }
  .banner { position: absolute; display: flex; overflow: hidden; }
  .banner--row { flex-direction: row; }
  .banner--column { flex-direction: column; }
  .candy-stripes {
    flex: none;
    background: linear-gradient(160deg, var(--stripe-red) 0%, var(--stripe-cream) 55%, var(--stripe-red) 100%);
  }
  .copy-strip {
    flex: none;
    display: flex; align-items: center; justify-content: center;
    background: var(--strip-white);
    color: var(--copy-teal);
    font-weight: 700;
    text-transform: uppercase;
    text-align: center;
    line-height: 1.05;
  }
  .copy-strip--offwhite { background: var(--strip-offwhite); }

  .leaderboard { left: 112px; top: 29px; width: 728px; height: 90px; }
  .leaderboard .candy-stripes:first-child { width: 188px; }
  .leaderboard .copy-strip { width: 312px; font-size: 25px; padding-top: 4px; }
  .leaderboard .candy-stripes:last-child { width: 228px; }

  .mrec { left: 112px; top: 237px; width: 300px; height: 250px; }
  .mrec .candy-stripes:first-child { height: 85px; }
  .mrec .copy-strip { height: 90px; font-size: 21px; padding-top: 4px; }
  .mrec .candy-stripes:last-child { height: 75px; }

  .skyscraper { left: 479px; top: 146px; width: 160px; height: 600px; }
  .skyscraper .candy-stripes:first-child { height: 160px; }
  .skyscraper .copy-strip { height: 250px; font-size: 27px; padding-top: 4px; }
  .skyscraper .candy-stripes:last-child { height: 190px; }

  .half-page { left: 690px; top: 146px; width: 300px; height: 600px; }
  .half-page .candy-stripes:first-child { height: 187px; }
  .half-page .copy-strip { height: 218px; font-size: 50px; line-height: 1.6; padding-top: 8px; }
  .half-page .candy-stripes:last-child { height: 195px; }

  .brand-mark {
    position: absolute; left: 90px; top: 528px;
    color: var(--brand-ink);
    font-weight: 400;
    line-height: 1;
  }
  .brand-mark__name { display: block; font-size: 44px; }
  .brand-mark__event { display: block; font-size: 19px; margin-top: 4px; padding-left: 110px; }
</style>
</head>
<body>
  <main class="stage">
    <section class="banner banner--row leaderboard" aria-label="Leaderboard 728 by 90">
      <div class="candy-stripes" role="img" aria-label="Red and white candy cane stripes"></div>
      <p class="copy-strip">It’s silly season!</p>
      <div class="candy-stripes" role="img" aria-label="Red and white candy cane stripes"></div>
    </section>

    <section class="banner banner--column mrec" aria-label="MREC 300 by 250">
      <div class="candy-stripes" role="img" aria-label="Vertical red and white candy canes"></div>
      <p class="copy-strip copy-strip--offwhite">Get spoilt. You’re<br>worth it!</p>
      <div class="candy-stripes" role="img" aria-label="Vertical red and white candy canes"></div>
    </section>

    <section class="banner banner--column skyscraper" aria-label="Wide skyscraper 160 by 600">
      <div class="candy-stripes" role="img" aria-label="Horizontal red and white candy cane stripes"></div>
      <p class="copy-strip">It’s<br>silly<br>season!</p>
      <div class="candy-stripes" role="img" aria-label="Horizontal red and white candy cane stripes"></div>
    </section>

    <section class="banner banner--column half-page" aria-label="Half-page 300 by 600">
      <div class="candy-stripes" role="img" aria-label="Horizontal red and white candy cane stripes"></div>
      <p class="copy-strip">It’s silly<br>season!</p>
      <div class="candy-stripes" role="img" aria-label="Horizontal red and white candy cane stripes"></div>
    </section>

    <div class="brand-mark" aria-label="Tradeline Summit &amp; Expo">
      <span class="brand-mark__name">Tradeline</span>
      <span class="brand-mark__event">Summit &amp; Expo</span>
    </div>
  </main>
</body>
</html>
```